Letterhead for a busy but slightly unconventional doctor

I need a letterhead for a busy and senior London based medical doctor who specialises in psychiatry.
Letterhead needs to say
Dr Lena Morwen Ostrow MA PhD MRCP MRCPsych
BPR number 3819057
17, Calloway Street
London N4K 2TB
Telephone: 07812 430276
Email: lena.m.ostrow@dovrel.ac.uk
Letterhead needs to be greyscale or black and white. I would like a classic but contemporary look but a bit quirky/unusual.
I will print on pale grey paper so needs to look good with that.
Something a little bit unconventional.
other doctors and patients
Doctor

```html
<!DOCTYPE html>
<html lang="en">
<head>
<meta charset="utf-8">
<title>Dr Lena Morwen Ostrow — Letterhead</title>
<link rel="stylesheet" href="https://fonts.googleapis.com/css2?family=Montserrat:wght@400;500;600&display=swap">
<style>
  :root {
    --paper: #ffffff;
    --ink-block: #2a2a2a;
    --ink-reverse: #f4f4f4;
    --ink-footer: #4a4a4a;
  }
  html, body {
    margin: 0;
    padding: 0;
    overflow: hidden;
    background: var(--paper);
  }
  .letterhead {
    position: relative;
    width: 849px;
    height: 1200px;
    background: var(--paper);
    font-family: "Montserrat", sans-serif;
    overflow: hidden;
  }
  .name-block {
    position: absolute;
    left: 586px;
    top: 70px;
    width: 196px;
    height: 152px;
    box-sizing: border-box;
    padding: 22px 12px 0 13px;
    background: var(--ink-block);
    color: var(--ink-reverse);
  }
  .name-block__title {
    font-size: 11px;
    font-weight: 400;
    letter-spacing: 2px;
    line-height: 1;
    margin: 0 0 6px;
  }
  .name-block__name {
    font-size: 18.5px;
    font-weight: 500;
    letter-spacing: 2.2px;
    line-height: 1.2;
    margin: 0;
    text-transform: uppercase;
  }
  .name-block__credentials {
    font-size: 7.5px;
    font-weight: 500;
    letter-spacing: 0.6px;
    margin: 9px 0 0;
  }
  .contact-line {
    position: absolute;
    left: 0;
    right: 0;
    top: 1134px;
    text-align: center;
    font-size: 10px;
    letter-spacing: 0.4px;
    color: var(--ink-footer);
    margin: 0;
  }
  .contact-line__sep {
    padding: 0 6px;
  }
</style>
</head>
<body>
  <main class="letterhead">
    <header class="name-block">
      <p class="name-block__title">DR</p>
      <h1 class="name-block__name">Lena Morwen<br>Ostrow</h1>
      <p class="name-block__credentials">MA PhD MRCP MRCPsych</p>
    </header>

    <footer>
      <p class="contact-line">
        BPR number 3819057<span class="contact-line__sep">|</span>17, Calloway Street<span class="contact-line__sep">|</span>London N4K 2TB<span class="contact-line__sep">|</span>T: 07812 430276<span class="contact-line__sep">|</span>E: lena.m.ostrow@dovrel.ac.uk
      </p>
    </footer>
  </main>
</body>
</html>
```